SEO AND WEB DESIGN COMPANY BUSINESS CARD DESIGN

I need an eye catching , simple business card design that will match my logo . I need 2 versions of it ( white background and black background) - SOME PEOPLE DID NOT GET IT AND SENDING US FRONT WHITE BACK WHITE VERSIONS WHICH IS NOT CORRECT.

ONE VERSION SHOULD BE BACK AND FRONT ALL BLACK , SECOND VERSION SHOULD BE BACK AND FRONT ALL WHITE

logo psd files are attached for both versions. The business card is going to have : First Name- Last name - position - phone numbers

```html
<!DOCTYPE html>
<html lang="en">
<head>
<meta charset="utf-8">
<title>Northline Studio – Business Cards</title>
<link rel="stylesheet" href="https://fonts.googleapis.com/css2?family=Roboto:wght@400;700;900&display=swap">
<style>
  :root {
    --stage: #1e1e1f;
    --card-dark: #222022;
    --card-light: #ffffff;
    --brand-blue: #5a8fd0;
    --ink: #111111;
    --ink-soft: #2b2b2b;
    --ink-on-dark: #e4e4e6;
    --white: #ffffff;
  }
  * { box-sizing: border-box; margin: 0; padding: 0; }
  html, body {
    width: 1200px;
    height: 900px;
    overflow: hidden;
    background: var(--stage);
    font-family: "Roboto", Arial, sans-serif;
  }
  .stage {
    width: 1200px;
    height: 900px;
    display: flex;
    flex-direction: column;
    align-items: center;
    justify-content: center;
    gap: 40px;
  }
  .card {
    --card-text: var(--ink-soft);
    --card-title: var(--ink);
    position: relative;
    width: 640px;
    height: 366px;
    overflow: hidden;
    box-shadow: 0 14px 30px rgba(0, 0, 0, 0.55);
  }
  .card--dark {
    background: var(--card-dark);
    --card-text: var(--ink-on-dark);
    --card-title: var(--white);
  }
  .card--light { background: var(--card-light); }

  .brand {
    position: absolute;
    top: 70px;
    left: 0;
    right: 0;
    display: flex;
    align-items: center;
    justify-content: center;
    gap: 16px;
  }
  .brand__dot {
    width: 34px;
    height: 34px;
    border-radius: 50%;
    background: var(--brand-blue);
    flex: none;
  }
  .brand__name {
    font-size: 48px;
    font-weight: 900;
    letter-spacing: 0.5px;
    line-height: 1;
    color: var(--card-title);
  }

  .contact {
    position: absolute;
    top: 170px;
    left: 0;
    right: 0;
    display: flex;
    justify-content: center;
    align-items: stretch;
    gap: 22px;
  }
  .person { text-align: right; padding-top: 4px; }
  .person__name {
    font-size: 30px;
    font-weight: 900;
    color: var(--brand-blue);
    line-height: 1;
  }
  .person__role {
    font-size: 18px;
    font-weight: 400;
    color: var(--card-text);
    margin-top: 2px;
  }
  .divider {
    width: 2px;
    background: var(--brand-blue);
  }
  .phones { list-style: none; }
  .phones li {
    display: flex;
    align-items: center;
    gap: 10px;
    font-size: 16px;
    color: var(--card-text);
    line-height: 24px;
  }
  .phones svg { width: 20px; height: 16px; flex: none; fill: var(--brand-blue); }

  .address-band {
    position: absolute;
    left: 0;
    right: 0;
    top: 270px;
    height: 46px;
    background: var(--brand-blue);
    color: var(--white);
    font-size: 16px;
    display: flex;
    align-items: center;
    justify-content: center;
  }
</style>
</head>
<body>
<main class="stage">
  <section class="card card--dark" aria-label="Business card, all-black version">
    <div class="brand">
      <span class="brand__dot"></span>
      <span class="brand__name">Northline Studio</span>
    </div>
    <div class="contact">
      <div class="person">
        <p class="person__name">Daniel Reyes</p>
        <p class="person__role">President</p>
      </div>
      <span class="divider"></span>
      <ul class="phones">
        <li><svg viewBox="0 0 20 16" aria-hidden="true"><path d="M1 5c0-3 18-3 18 0v2h-5V5H6v2H1z M4 8h12l2 7H2z"/></svg>+00 000 000 0000</li>
        <li><svg viewBox="0 0 20 16" aria-hidden="true"><path d="M1 5c0-3 18-3 18 0v2h-5V5H6v2H1z M4 8h12l2 7H2z"/></svg>+00 000 000 0000</li>
        <li><svg viewBox="0 0 20 16" aria-hidden="true"><path d="M1 5c0-3 18-3 18 0v2h-5V5H6v2H1z M4 8h12l2 7H2z"/></svg>+00 000 000 0000</li>
      </ul>
    </div>
    <p class="address-band">00000 Your Address St. Suite 0000 Address, NY 00000</p>
  </section>

  <section class="card card--light" aria-label="Business card, all-white version">
    <div class="brand">
      <span class="brand__dot"></span>
      <span class="brand__name">Northline Studio</span>
    </div>
    <div class="contact">
      <div class="person">
        <p class="person__name">Daniel Reyes</p>
        <p class="person__role">President</p>
      </div>
      <span class="divider"></span>
      <ul class="phones">
        <li><svg viewBox="0 0 20 16" aria-hidden="true"><path d="M1 5c0-3 18-3 18 0v2h-5V5H6v2H1z M4 8h12l2 7H2z"/></svg>+00 000 000 0000</li>
        <li><svg viewBox="0 0 20 16" aria-hidden="true"><path d="M1 5c0-3 18-3 18 0v2h-5V5H6v2H1z M4 8h12l2 7H2z"/></svg>+00 000 000 0000</li>
        <li><svg viewBox="0 0 20 16" aria-hidden="true"><path d="M1 5c0-3 18-3 18 0v2h-5V5H6v2H1z M4 8h12l2 7H2z"/></svg>+00 000 000 0000</li>
      </ul>
    </div>
    <p class="address-band">00000 Your Address St. Suite 0000 Address, NY 00000</p>
  </section>
</main>
</body>
</html>
```